Website for a start-up named Vlm Quarvex.

The company is currently producing a sustainable tactical training measure for soldiers in the defense industry. We’d like a simple website design. As the product hasn’t been launched yet, we will not tell too much about the product and it’s not for sale either. We have a website on wix called vlmquarvex.com which we would like to proceed with. The design just needs a professional and loving touch. We develop an add on for TK40 rifles.

Target Market(s)

Defense industry

Industry/Entity Type

Defense

Coding

Coded - Design and coding required

Number of Pages Required

1 page

```html
<!DOCTYPE html>
<html lang="en">
<head>
<meta charset="utf-8">
<title>Vlm Quarvex</title>
<link rel="stylesheet" href="https://fonts.googleapis.com/css2?family=Audiowide&family=Nunito+Sans:wght@300;400;600;700&family=Montserrat:wght@700&family=Barlow:ital,wght@1,400&display=swap">
<style>
:root{
  --teal:#0aa89e;
  --teal-dark:#078a82;
  --ink:#0b1419;
  --panel:#0f1c23;
  --panel-2:#101a20;
  --text:#ffffff;
  --muted:#b8c3c7;
  --grey-text:#3b4246;
  --footer-text:#8b969b;
}
*{box-sizing:border-box;margin:0;padding:0}
html,body{width:1200px;height:3247px;overflow:hidden;background:var(--ink)}
body{position:relative;font-family:"Nunito Sans",sans-serif;color:var(--text)}
.abs{position:absolute}
.display{font-family:"Audiowide",sans-serif;color:var(--teal);font-weight:400;line-height:1;white-space:nowrap}
.eyebrow{font-family:"Audiowide",sans-serif;font-size:15px;letter-spacing:9px;color:var(--text)}
.btn{position:absolute;display:flex;align-items:center;justify-content:center;font-family:"Montserrat",sans-serif;font-weight:700;font-size:13px;letter-spacing:2.5px;color:#fff;background:var(--teal);clip-path:polygon(12px 0,100% 0,calc(100% - 12px) 100%,0 100%)}
.photo{position:absolute}

/* hero */
.hero{position:absolute;left:0;top:0;width:1200px;height:637px;background:radial-gradient(ellipse at 75% 40%,#1a262b 0%,#0c1215 55%,#050708 100%)}
.hero-photo{left:170px;top:70px;width:500px;height:567px;
  background:
    radial-gradient(ellipse 22% 14% at 48% 20%,rgba(150,120,80,.55),rgba(0,0,0,0) 100%),
    radial-gradient(ellipse 30% 22% at 38% 45%,rgba(160,130,90,.45),rgba(0,0,0,0) 100%),
    radial-gradient(ellipse 45% 50% at 45% 45%,#4a4432 0%,#2c2a22 45%,rgba(8,10,10,0) 80%)}
.brand{position:absolute;left:161px;top:38px;font-family:"Audiowide",sans-serif;font-size:20px;line-height:30px;color:var(--teal);display:flex;align-items:center;gap:8px;white-space:nowrap}
.brand .dot{width:10px;height:10px;border-radius:50%;background:var(--teal)}
.nav{position:absolute;top:44px;left:0;font-size:14px;color:#fff}
.nav a{position:absolute;white-space:nowrap;color:#fff;text-decoration:none}
.nav a.active{color:var(--teal)}
.book{left:917px;top:35px;width:119px;height:36px;font-family:"Nunito Sans",sans-serif;font-size:14px;letter-spacing:0}
.rail{left:176px;top:111px;width:1px;height:510px;background:#5f6a6e}
.slide-dot{position:absolute;width:30px;height:30px;border-radius:50%;display:flex;align-items:center;justify-content:center;font-size:13px;background:var(--ink)}
.hero-lead{left:631px;top:280px;font-family:"Audiowide",sans-serif;font-size:15px}
.hero-title{left:631px;top:308px;font-size:44px;line-height:54px}

/* welcome */
.welcome{position:absolute;left:0;top:637px;width:1200px;height:538px;background:var(--panel)}
.p-body{font-size:13.5px;line-height:20px;color:var(--muted);font-weight:300}

/* rifles band */
.band{position:absolute;left:0;top:1175px;width:1200px;height:216px;
  background:radial-gradient(ellipse 30% 60% at 62% 90%,rgba(40,70,110,.55),rgba(0,0,0,0)),linear-gradient(90deg,#2a241c,#3a2f22 40%,#1c252b 70%,#141c22)}
.band-teal{position:absolute;left:0;top:0;width:561px;height:216px;background:var(--teal);clip-path:polygon(0 0,561px 0,479px 216px,0 216px)}
.rifle{left:220px;top:1254px;width:442px;height:176px;border-radius:6px;
  background:radial-gradient(ellipse 60% 40% at 50% 50%,#2a2d2f,#141617 70%,#0d0f10)}

/* who we are */
.who{position:absolute;left:0;top:1391px;width:1200px;height:474px;background:#fff}
.who-photo{left:607px;top:68px;width:426px;height:337px;
  background:
    radial-gradient(ellipse 40% 20% at 55% 95%,rgba(40,170,150,.45),rgba(0,0,0,0)),
    radial-gradient(ellipse 35% 25% at 55% 62%,rgba(200,170,150,.35),rgba(0,0,0,0)),
    linear-gradient(180deg,#5a605b 0%,#3b403d 28%,#1e2324 40%,#2e3234 62%,#0c1a1b 100%)}

/* technology */
.tech{position:absolute;left:0;top:1865px;width:1200px;height:481px;background:var(--panel-2)}
.tech-photo{left:161px;top:73px;width:404px;height:339px;
  background:
    radial-gradient(ellipse 22% 25% at 70% 28%,rgba(190,150,120,.6),rgba(0,0,0,0)),
    radial-gradient(ellipse 35% 30% at 70% 75%,rgba(110,120,110,.6),rgba(0,0,0,0)),
    linear-gradient(100deg,#c9cfd0 0%,#9aa2a3 20%,#4c5453 42%,#2f3535 70%,#23292a 100%)}

/* testimonials */
.testi{position:absolute;left:0;top:2346px;width:1200px;height:531px;background:radial-gradient(ellipse at 50% 50%,#1b2328,#0b1114 80%)}
.quote-card{left:292px;top:2562px;width:613px;height:210px}

/* footer */
.footer{position:absolute;left:0;top:2877px;width:1200px;height:318px;background:var(--panel)}
.foot-h{position:absolute;font-family:"Audiowide",sans-serif;font-size:15px;font-weight:400;color:var(--teal)}
.foot-t{position:absolute;font-size:13px;color:var(--footer-text);line-height:20px}
.social{position:absolute;top:2995px;width:40px;height:35px;background:#162329;display:flex;align-items:center;justify-content:center}
.social span{width:10px;height:10px;background:#fff}
.legal{position:absolute;left:0;top:3195px;width:1200px;height:52px;background:#0a1216;text-align:center;line-height:52px;font-size:12px;color:#5c676c}
</style>
</head>
<body>

<section class="hero">
  <div class="photo hero-photo" role="img" aria-label="Armed soldier in tactical gear kneeling with a rifle in smoke"></div>
  <div class="brand"><span class="dot"></span>Vlm Quarvex</div>
  <nav class="nav">
    <a class="active" style="left:365px">Home</a>
    <a style="left:439px">About us</a>
    <a style="left:531px">Products</a>
    <a style="left:621px">Who we are</a>
    <a style="left:731px">Technology</a>
    <a style="left:838px">Contact Us</a>
  </nav>
  <div class="btn book">Book Online</div>
  <div class="abs rail"></div>
  <div class="slide-dot" style="left:161px;top:330px;border:1px solid var(--teal);color:var(--teal)">1</div>
  <div class="slide-dot" style="left:163px;top:373px;width:26px;height:26px;border:2px solid #fff;color:#fff">2</div>
  <p class="abs hero-lead">Offering scalable solutions for the</p>
  <h1 class="abs display hero-title">Defense and<br>Security Industry</h1>
  <div class="btn" style="left:636px;top:431px;width:145px;height:35px">READ MORE</div>
</section>

<section class="welcome">
  <p class="abs eyebrow" style="left:161px;top:110px">Welcome to</p>
  <h2 class="abs display" style="left:161px;top:138px;font-size:46px">Vlm Quarvex</h2>
  <p class="abs" style="left:161px;top:201px;font-size:17px">Sustainable solutions to the defense industry</p>
  <p class="abs p-body" style="left:161px;top:233px;width:350px">Welcome to Vlm Quarvex, the advanced Technology Company paving the way to the future. We are a team of like-minded and determined individuals, all sharing a vision for success. We believe that our sophisticated technology has the potential to become an industry sensation. Would you like to find out more? Our website will be updated on a regular basis</p>
  <div class="btn" style="left:163px;top:399px;width:160px;height:35px">GET IN TOUCH</div>
  <div class="photo" style="left:573px;top:93px;width:467px;height:328px;background:radial-gradient(ellipse 30% 35% at 70% 35%,rgba(120,170,165,.55),rgba(0,0,0,0)),radial-gradient(ellipse 22% 25% at 25% 42%,rgba(140,170,165,.45),rgba(0,0,0,0)),radial-gradient(ellipse 35% 10% at 48% 80%,rgba(190,230,225,.5),rgba(0,0,0,0)),linear-gradient(180deg,#5c6450,#3a4236 50%,#1c2220)" role="img" aria-label="Soldier in camouflage holding a holographic tablet display"></div>
</section>

<section class="band">
  <div class="band-teal"></div>
  <p class="abs eyebrow" style="left:698px;top:68px">Our</p>
  <h2 class="abs display" style="left:698px;top:107px;font-size:44px">TK40 Rifles</h2>
</section>
<div class="photo rifle" role="img" aria-label="TK40 rifle with an add-on attachment, side view"></div>

<section class="who">
  <h2 class="abs display" style="left:161px;top:118px;font-size:44px">Who we are</h2>
  <p class="abs" style="left:161px;top:175px;width:325px;font-size:13.5px;line-height:21.4px;color:var(--grey-text);font-weight:300">Vlm Quarvex is a leading provider of cutting-edge technologies and services, offering scalable solutions for the defense and security industry of all sizes. Founded by a group of friends who started by scribbling their ideas on a bus ride in San Francisco. Today we are working on innovative solutions to disrupt the training industry with a sustainable solution.</p>
  <div class="photo who-photo" role="img" aria-label="Soldier typing on a laptop showing code"></div>
  <div class="abs" style="left:525px;top:189px;width:162px;height:119px;background:linear-gradient(135deg,var(--teal),var(--teal-dark))"></div>
</section>

<section class="tech">
  <div class="photo tech-photo" role="img" aria-label="Soldier with headset operating a joystick at a control station"></div>
  <p class="abs eyebrow" style="left:610px;top:100px">OUR INNOVATIVE</p>
  <h2 class="abs display" style="left:610px;top:128px;font-size:46px">Technology</h2>
  <p class="abs" style="left:611px;top:211px;font-size:17px">The Possibilities Are Endless</p>
  <p class="abs p-body" style="left:611px;top:244px;width:350px">At Vlm Quarvex, our comprehensive technological solutions help the industry to become more sustainable and efficient with the spendings. We will balance qualitative training experience for soldiers and security forces with real life experiences and a real life feel.</p>
  <div class="btn" style="left:612px;top:375px;width:159px;height:36px">READ MORE</div>
</section>

<section class="testi">
  <p class="abs eyebrow" style="left:0;width:1200px;text-align:center;top:80px">Client</p>
  <h2 class="abs display" style="left:0;width:1200px;text-align:center;top:108px;font-size:46px">Testimonials</h2>
</section>
<svg class="abs quote-card" viewBox="0 0 613 210" aria-hidden="true">
  <polygon points="54,0 613,0 559,210 0,210" fill="#0aa89e"/>
  <polygon points="66,7 602,7 550,203 11,203" fill="none" stroke="#ffffff" stroke-width="1.2" opacity="0.85"/>
  <text x="306" y="86" text-anchor="middle" font-family="Georgia,serif" font-size="90" font-weight="700" fill="#fff">&#8220;</text>
</svg>
<p class="abs" style="left:0;width:1200px;text-align:center;top:2652px;font-family:'Barlow',sans-serif;font-style:italic;font-size:22px">The secret of getting ahead is getting started</p>
<p class="abs" style="left:0;width:1200px;text-align:center;top:2699px;font-family:'Audiowide',sans-serif;font-size:18px">Elias Brandt</p>

<footer class="footer">
  <div class="brand" style="top:88px;font-size:22px"><span class="dot"></span>Vlm Quarvex</div>
  <p class="foot-t" style="left:161px;top:140px;width:240px">Welcome to Vlm Quarvex, the advanced Technology Company paving the way to the future. We are a team of like-minded and determined individuals</p>

  <h3 class="foot-h" style="left:469px;top:76px">Contact Info</h3>
  <svg class="abs" style="left:470px;top:117px" width="11" height="15" viewBox="0 0 11 15"><path d="M5.5 0a5.5 5.5 0 0 0-5.5 5.5C0 9.6 5.5 15 5.5 15S11 9.6 11 5.5A5.5 5.5 0 0 0 5.5 0zm0 7.6a2.1 2.1 0 1 1 0-4.2 2.1 2.1 0 0 1 0 4.2z" fill="#0aa89e"/></svg>
  <p class="foot-t" style="left:491px;top:114px;width:135px">K. L. Venstrups Vej 14, 2.</p>
  <svg class="abs" style="left:470px;top:175px" width="13" height="13" viewBox="0 0 24 24"><path d="M6.6 10.8a15.1 15.1 0 0 0 6.6 6.6l2.2-2.2a1 1 0 0 1 1-.25 11.4 11.4 0 0 0 3.6.57 1 1 0 0 1 1 1V20a1 1 0 0 1-1 1A17 17 0 0 1 3 4a1 1 0 0 1 1-1h3.5a1 1 0 0 1 1 1c0 1.25.2 2.45.57 3.57a1 1 0 0 1-.25 1z" fill="#0aa89e"/></svg>
  <p class="foot-t" style="left:491px;top:172px">+45 38176420</p>
  <svg class="abs" style="left:470px;top:217px" width="13" height="10" viewBox="0 0 13 10"><rect width="13" height="10" rx="1" fill="#0aa89e"/><path d="M0.5 1l6 4.5 6-4.5" stroke="#0f1c23" stroke-width="1.3" fill="none"/></svg>
  <p class="foot-t" style="left:491px;top:212px">info@vlmquarvex.com</p>

  <h3 class="foot-h" style="left:730px;top:76px">Quick Links</h3>
  <p class="foot-t" style="left:730px;top:114px">Home</p>
  <p class="foot-t" style="left:730px;top:142px">About us</p>
  <p class="foot-t" style="left:730px;top:170px">Products</p>
  <p class="foot-t" style="left:730px;top:198px">Who we are</p>
  <p class="foot-t" style="left:730px;top:226px">Technology</p>
  <p class="foot-t" style="left:730px;top:254px">Contact Us</p>

  <h3 class="foot-h" style="left:908px;top:76px">Follow Us</h3>
</footer>
<div class="social" style="left:910px" aria-label="Social link"><span></span></div>
<div class="social" style="left:955px" aria-label="Social link"><span></span></div>
<div class="social" style="left:1000px" aria-label="Social link"><span></span></div>

<div class="legal">© 2021 <span style="color:var(--teal)">Vlm Quarvex</span> All rights reserved.</div>

</body>
</html>
```